Herb Farm - Tea Label Design

We are a small herbalist company called 'Meadowlark Remedies' which requires a new label scheme.

Meadowlark Remedies specializes in organic wellness teas, handmade soaps, bath and beauty products. We also offer local beeswax, pollen and an herb CSA.

Our slogan is "Ancient Remedies for Modern Life" and we frequently market ourselves as an "Apothecary & Herb Farm".

The primary use of this label will be on tins and biodegradable food grade paper bags.

We are looking for:

1) An unique universal design for our products. Something that we can put on the tea tins/bags as well as boxes in the future. To keep costs down I would like something that can be used on a variety of products by simply having the colour changed or adding the title of the product in a certain area. We have four collections. Please see the attached style guide. I particularly like the Silverbrook Leaf Co. as each type of tea is reprinted by a design. Please see their website for further clarification. I also really like their styling.

2) Label required is 8.5" x 5.25" (w - h). Bear in mind we also have dark cobalt blue jars and Kraft biodegradable bags available that this label will fit on (5570-02 as pictured)

3) We would like to see a design that is colourful, and has elements of modern simplicity yet certainly has an old world apothecary charm.

4) Please refer to our current label for product information. Not everything has to be in the same place in the new design, however all the information is required.

We will require source files in .ai and .eps (layers retained, no outlines on text, list of fonts used).

Please visit: www.meadowlarkremedies.example

We included a few favourites and the styles we prefer, but please be creative!

The label chosen could be in for a lot more design work as we expand our company. Any other input regarding packaging would be helpful.
Updates

Hello Designers!

I have posted our current label for you to review - I like it, yet I don't. You can see the level of craftsman ship brings up to artisan, and mid-high range product. The only parts I really want to keep from this label is how the brewing instructions are set out.

In terms of design, I do not want to use a photograph on the label - it is there for inspiration!

Thanks,
Meadowlark Remedies 

Reason: I would like to see more designs, from a variety of designers for this label project.

Reason: Would like to see more designs.

Reason: In receiving designs I realized that the sizing is not ideal as it does not have ample space for the required information. I have updated the brief to reflect this and posted a working file that has the required elements. A lot of good designs, but I noticed the over use of filigree or Victorian ornamentation. I would like some ornamentation but simplicity is desired in the overall label. There was not enough designs submitted, nothing that truly wow-ed me. I hope to see more unique designs! Thanks.

Target Market(s)

30-something, retired, eco-conscious, women, mid-priced marketing, local Ontario Canada; some products will be sold at a local historical village

Industry/Entity Type

Biodegradable

Font styles to use
Decorative
Other font styles liked:
• DellaRobbia BT Bold; Foglihten No07

Requirements
Must have
• Fonts used: Dellarobbia BT Bold and Foglihten No07
Use fonts and logo design; you can use separate leaf components but fonts chosen for logo cannot change

Other fonts can be used but please use Foglihten No07 for "Meadowlark Remedies" and Dellarobbia BT Bold for "Apothecary & Herb Farm" and for "Ancient Remedies for Modern Life".
Nice to have
• "Apothecary & Herb Farm" or slogan
Should not have
• Comic sans
clipart
Filigree or line swooshes

```html
<!DOCTYPE html>
<html lang="en">
<head>
<meta charset="utf-8">
<title>Meadowlark Remedies – Collection Labels</title>
<link rel="stylesheet" href="https://fonts.googleapis.com/css2?family=Della+Respira&family=Federo&display=swap">
<style>
  :root {
    --page: #ffffff;
    --highland-bg: #6fa7c9;
    --heather-bg: #c29a9b;
    --cream: #fcf5b2;
    --arch-green: #14884f;
    --gold: #e6c231;
    --gold-soft: #eadb8c;
    --highland-accent: #4a55a8;
    --heather-accent: #9a4a5a;
    --sprig-highland: #5577a8;
    --sprig-heather: #b9588a;
  }
  html, body {
    margin: 0;
    padding: 0;
    width: 1200px;
    height: 1000px;
    overflow: hidden;
    background: var(--page);
  }
  .canvas {
    position: relative;
    width: 1200px;
    height: 1000px;
  }
  .label {
    position: absolute;
    width: 625px;
    height: 416px;
    display: block;
  }
  .label--highland { left: 296px; top: 66px; }
  .label--heather { left: 295px; top: 524px; }
  .collection-name {
    font-family: "Della Respira", serif;
    font-size: 11.5px;
    letter-spacing: 3px;
    fill: var(--arch-green);
  }
  .brand-name {
    font-family: "Federo", sans-serif;
    font-size: 35px;
    fill: var(--arch-green);
  }
  .tagline {
    font-family: "Della Respira", serif;
    font-size: 17px;
  }
  .label--highland .tagline { fill: var(--highland-accent); }
  .label--heather .tagline { fill: var(--heather-accent); }
</style>
</head>
<body>
<main class="canvas">

  <svg class="label label--highland" viewBox="0 0 625 416" aria-label="Highland Collection label">
    <rect class="label-backdrop" width="625" height="416" fill="var(--highland-bg)" role="img" aria-label="Vintage botanical engraving pattern of leaves, fruits and flowers on blue"/>
    <path class="arch-plate" d="M131 323 V250 A186 186 0 0 1 503 250 V323 Z" fill="var(--cream)"/>
    <path class="arch-frame" d="M138 316 V250 A179 179 0 0 1 496 250 V316 Z" fill="none" stroke="var(--arch-green)" stroke-width="3"/>
    <path class="arch-inner" d="M177 248 A140 140 0 0 1 457 248" fill="none" stroke="var(--gold)" stroke-width="1.5"/>
    <circle cx="177" cy="248" r="3.5" fill="var(--gold)"/>
    <circle cx="457" cy="248" r="3.5" fill="var(--gold)"/>
    <line class="collection-rule" x1="225" y1="155" x2="410" y2="155" stroke="var(--gold-soft)" stroke-width="1"/>
    <text class="collection-name" x="317" y="136" text-anchor="middle">HIGHLAND</text>
    <text class="collection-name" x="317" y="150" text-anchor="middle">COLLECTION</text>
    <ellipse class="sprig" cx="330" cy="197" rx="48" ry="32" fill="var(--sprig-highland)" opacity="0.75" role="img" aria-label="Watercolour herb sprigs in blue"/>
    <text class="brand-name" x="317" y="273" text-anchor="middle">Meadowlark Remedies</text>
    <text class="tagline" x="317" y="298" text-anchor="middle">Apothecary &amp; Herb Farm</text>
  </svg>

  <svg class="label label--heather" viewBox="0 0 625 416" aria-label="Heather Collection label">
    <rect class="label-backdrop" width="625" height="416" fill="var(--heather-bg)" role="img" aria-label="Vintage botanical engraving pattern of leaves, fruits and flowers on dusty rose"/>
    <path class="arch-plate" d="M131 323 V250 A186 186 0 0 1 503 250 V323 Z" fill="var(--cream)"/>
    <path class="arch-frame" d="M138 316 V250 A179 179 0 0 1 496 250 V316 Z" fill="none" stroke="var(--arch-green)" stroke-width="3"/>
    <path class="arch-inner" d="M166 244 A151 151 0 0 1 452 244" fill="none" stroke="var(--gold)" stroke-width="1.5"/>
    <circle cx="166" cy="218" r="3.5" fill="var(--gold)"/>
    <circle cx="450" cy="212" r="3.5" fill="var(--gold)"/>
    <line class="collection-rule" x1="212" y1="148" x2="420" y2="148" stroke="var(--gold-soft)" stroke-width="1"/>
    <text class="collection-name" x="317" y="129" text-anchor="middle">HEATHER</text>
    <text class="collection-name" x="317" y="143" text-anchor="middle">COLLECTION</text>
    <ellipse class="sprig" cx="320" cy="193" rx="48" ry="32" fill="var(--sprig-heather)" opacity="0.75" role="img" aria-label="Watercolour herb sprigs in pink and violet"/>
    <text class="brand-name" x="304" y="275" text-anchor="middle">Meadowlark Remedies</text>
    <text class="tagline" x="302" y="296" text-anchor="middle">Apothecary &amp; Herb Farm</text>
  </svg>

</main>
</body>
</html>
```